energy rating company

Web Design graphics and layout only

To create two pages for the website. First the home page and the second is the design for the job board for our clients use after login. I have attached files that explain in detail what the pages should have and the purpose/desires of each object. Please read these thoroughly.

The webpages need to be clean, professional, easy on the eye, obvious in all its buttons and functions with a strong call to action on the home page and branding and clean, great and obvious looking buttons and very simple but dynamic as well. We wish to be seen as contemporary.

Business Concept

Our business concept is simple, to build a website whereby our clients will be able to upload jobs for energy raters to quote on and subsequent complete the work if their quote is selected. To link energy ratings that are required with energy raters via our website. Similarly to the varn website, jobs will be “advertised” on the job board and raters will select which jobs they wish to quote for.

I have attached a Word document explaining all the parts of the website and another word document showing what we are sort of after and a excel spreadsheet as well. Please read these in conjunction with this brief!
Updates

Dear All

I have submitted with my brief a word doc and excel spreadsheet of the two pages I want created.  However this is not the layout or design I want, I only put it together so that you will need to know what is required on each page.  Feel free to change and redesign it all.

Also the second page does not require the "process" logo or any other menu items except the first five being Home, How it works, About Us, testimonials and Contact us as per the home page.

We also are looking for something very professional and very clean.  It should be very easy to see exactly what you are looking for.

I will also extend the deadline for new designers!!  I am excited to see your talents!!

Thanks

I have increase budget and posted a note saying feel free to change all the details layout etc on my brief just include everything!!! 

Wanting a professional corporate look...

Want a professional corporate look

We have changed our minds and you we no longer require the process to be on the home page.

Thanks

Target Market(s)

Target Market

Home Inspection Companies
Pest Inspection Companies
Residential home buyers/sellers
Real Estate companies

Industry/Entity Type

It Company

Number of Pages Required

1 page

Requirements
Must have
• Colours and Styles

• The website should be mainly white as I believe it is seen as clean and simple with colour from the logos, but can be swayed if it projects the image we are after.

• It should be obvious and process orientated and I do believe symbols, pictures, etc should replace words where possible.

```html
<!DOCTYPE html>
<html lang="en">
<head>
<meta charset="utf-8">
<title>Voltis Australia – Home and Job Board</title>
<link href="https://fonts.googleapis.com/css2?family=Jost:wght@300;400;500&family=Open+Sans:wght@400;600;700&display=swap" rel="stylesheet">
<style>
:root{
  --green:#2e8a2a;--green-dark:#1f6a1d;--green-light:#4aa83f;
  --orange:#e8661b;--orange-dark:#c9500f;--orange-text:#d0600f;
  --dark:#3b3b3b;--ink:#333;--muted:#8a8a8a;--row:#efefef;--row2:#f6f6f6;--line:#dcdcdc;
}
*{box-sizing:border-box;margin:0;padding:0}
html,body{width:1200px;height:2724px;overflow:hidden;background:#fff}
body{font-family:"Open Sans",sans-serif;color:var(--ink);position:relative}
.abs{position:absolute}
.page-title{position:absolute;left:0;width:1200px;text-align:center;font-family:"Jost",sans-serif;font-weight:300;font-size:44px;color:#333;letter-spacing:1px}
.green-bar{position:absolute;left:0;width:1200px;height:21px;background:linear-gradient(var(--green-light),var(--green-dark))}
.frame{position:absolute;left:113px;width:974px;background:#fff;box-shadow:0 0 14px rgba(0,0,0,.25)}
.header-bg{position:absolute;left:113px;width:974px;background:linear-gradient(#f8f8f8,#ececec)}
.nav{position:absolute;left:493px;width:571px;height:26px;background:linear-gradient(var(--green-light),var(--green));border-radius:0 0 4px 4px;display:flex;justify-content:center;align-items:center;gap:10px;font-family:"Jost",sans-serif;font-size:14px;color:#fff}
.nav span.sep{opacity:.8}
.logo-box{position:absolute;left:132px;width:311px;background:linear-gradient(#f4f4f4,#e8e8e8);box-shadow:2px 0 4px rgba(0,0,0,.15),-2px 0 4px rgba(0,0,0,.1);display:flex;align-items:center;padding-left:20px;gap:14px}
.logo-dot{width:70px;height:70px;border-radius:50%;background:var(--green-light)}
.logo-name{font-family:"Jost",sans-serif;font-weight:500;font-size:44px;color:var(--orange-dark);line-height:1}
.dark-band{position:absolute;left:0;width:1200px;background:linear-gradient(#3a3a3a,#555)}
.orange-area{position:absolute;left:113px;width:974px;background:linear-gradient(#d9560f,#f07a2a 70%,#f58a38)}
.fade{position:absolute;left:113px;width:974px;background:linear-gradient(#fbc9a0,#fff)}
.icon-item{position:absolute;width:140px;text-align:center;font-family:"Jost",sans-serif;font-size:13px;color:#333}
.icon-art{width:64px;height:64px;margin:0 auto 6px;border-radius:8px}
.icon-item small{display:block;font-size:8px;line-height:1}
.step{position:absolute;top:349px;height:106px;background:linear-gradient(#fff,#e6e6e6);border:1px solid #fff;border-radius:4px;box-shadow:0 2px 4px rgba(0,0,0,.3);padding:0 10px;font-family:"Jost",sans-serif;color:#666;display:flex;flex-direction:column;justify-content:flex-end;padding-bottom:8px}
.step b{font-weight:400;font-size:26px;color:var(--orange);line-height:1}
.step span{font-size:16px;line-height:1.1}
.step-num{position:absolute;top:-12px;left:-8px;width:24px;height:24px;border-radius:50%;background:#fff;border:1px solid #888;font-size:15px;color:#333;text-align:center;line-height:22px;font-family:"Jost",sans-serif}
.step-glow{position:absolute;top:460px;height:55px;background:linear-gradient(rgba(255,255,255,.25),rgba(255,255,255,0))}
h2.head{position:absolute;font-family:"Jost",sans-serif;font-weight:300;font-size:29px;color:var(--orange-text)}
.copy{position:absolute;font-size:12px;line-height:14px;color:#444}
.copy p{margin-bottom:14px}
.copy strong{color:var(--orange-dark)}
.photo{position:absolute;background:linear-gradient(#cfd3d4,#8d9293 60%,#6d7274)}
.bullets{position:absolute;left:148px;width:568px;top:840px;list-style:none}
.bullets li{height:25.4px;display:flex;align-items:center;font-size:12px;font-weight:600;letter-spacing:.3px;color:#333;background:linear-gradient(90deg,#f1f1f1,#fafafa)}
.bullets li::before{content:"";width:10px;height:10px;background:#333;margin:0 16px 0 8px}
.box{position:absolute;left:787px;width:260px;background:#f6f6f6;border:1px solid #e2e2e2;border-radius:4px;overflow:hidden}
.box-head{height:40px;background:linear-gradient(#f07d2c,var(--orange-dark));color:#fff;font-family:"Jost",sans-serif;font-weight:500;font-size:23px;text-align:center;line-height:40px}
.field-label{font-size:12px;font-weight:700;margin:8px 16px 4px}
.field{margin:0 26px 0 16px;height:27px;background:#fff;border:1px solid #d4d4d4}
.btn-green{display:block;background:linear-gradient(var(--green-light),var(--green-dark));color:#fff;font-weight:700;border-radius:3px;text-align:center}
.testi{padding:8px 16px;font-size:11px;line-height:17.5px;color:#8a8a8a}
.testi p{margin-bottom:18px}
.testi b{color:#777}
.footer{position:absolute;left:113px;width:974px;height:41px;background:linear-gradient(var(--green-light),var(--green-dark));display:flex;justify-content:flex-end;align-items:center;padding-right:34px;gap:7px;color:#fff;font-size:10px;font-weight:700}
.footer-side{position:absolute;left:0;width:1200px;height:41px;background:linear-gradient(#666,#333)}
.user-links{position:absolute;right:136px;top:1578px;font-size:13px;color:#222;display:flex;gap:10px}
.history{position:absolute;left:132px;top:1621px;width:938px;height:166px;background:rgba(255,210,170,.45);border:1px solid rgba(255,255,255,.35)}
.portrait{position:absolute;left:17px;top:10px;width:133px;height:143px;background:#fff;display:flex;align-items:center;justify-content:center;font-size:12px;color:#333}
.history h3{position:absolute;left:185px;top:18px;font-family:"Jost",sans-serif;font-weight:400;font-size:24px;color:#fff}
.history ul{position:absolute;left:186px;top:54px;list-style:none;font-size:12px;color:#fff;line-height:23.3px}
.edit-btn{position:absolute;left:768px;top:1877px;width:89px;height:25px;background:#1a1a1a;color:#fff;font-size:12px;font-weight:700;text-align:center;line-height:25px}
.account{position:absolute;left:148px;top:1910px;width:709px;border-collapse:separate;border-spacing:0 4px;font-size:12px;color:#444}
.account td{height:25px;background:var(--row);padding:0 5px}
.account td.label{width:129px;border-right:6px solid #fff}
.account td.value{padding-left:12px}
.tab{position:absolute;top:2175px;height:51px;font-family:"Jost",sans-serif;font-weight:500;font-size:17px;letter-spacing:.5px;text-align:center;line-height:51px;border-radius:4px 4px 0 0}
.tab.on{background:#1a1a1a;color:#fff}
.tab.off{background:#ededed;color:var(--orange)}
.jobs-panel{position:absolute;left:148px;top:2226px;width:905px;height:409px;background:#f2f2f2;border:1px solid #ddd}
.jobs-panel h4{position:absolute;left:20px;top:26px;font-size:12px;font-weight:700;color:#333}
.jobs{position:absolute;left:10px;top:60px;width:883px;border-collapse:collapse;font-size:12px;color:#444;text-align:center}
.jobs th{height:48px;background:linear-gradient(#d0d0d0,#b3b3b3);font-size:10px;font-weight:700;letter-spacing:.6px;line-height:12px;color:#555;border-right:1px solid #c6c6c6}
.jobs td{height:31px;border-right:1px solid #fff;border-bottom:1px solid #fff}
.jobs tr:nth-child(odd) td{background:#e6e6e6}
.jobs tr:nth-child(even) td{background:#ececec}
.mini{display:inline-block;width:56px;height:17px;line-height:17px;font-size:10px;font-weight:700;border-radius:2px;background:linear-gradient(var(--green-light),var(--green-dark));color:#fff;border:1px solid #1b5a18}
</style>
</head>
<body>

<!-- HOME PAGE -->
<div class="page-title" style="top:24px">HOME PAGE</div>
<div class="green-bar" style="top:98px"></div>
<div class="dark-band" style="top:303px;height:214px"></div>
<div class="footer-side" style="top:1238px"></div>
<div class="frame" style="top:118px;height:1160px"></div>
<div class="header-bg" style="top:118px;height:180px"></div>
<nav class="nav" style="top:118px"><span>HOME</span><span class="sep">|</span><span>HOW IT WORKS?</span><span class="sep">|</span><span>ABOUT US</span><span class="sep">|</span><span>TESTIMONIALS</span><span class="sep">|</span><span>CONTACT US</span></nav>
<div class="logo-box" style="top:118px;height:178px"><div class="logo-dot"></div><div class="logo-name">voltis<br><span style="font-size:22px;letter-spacing:2px">australia</span></div></div>

<div class="icon-item" style="left:570px;top:170px"><div class="icon-art" role="img" aria-label="Quote document illustration" style="background:linear-gradient(#cfe3f7,#5f95c9)"></div>GET A QUOTE</div>
<div class="icon-item" style="left:721px;top:170px"><div class="icon-art" role="img" aria-label="Energy raters illustration" style="background:linear-gradient(#c8b79a,#4f6b8c)"></div>ENERGY RATERS<small>ADD YOUR BUSINES</small></div>
<div class="icon-item" style="left:878px;top:170px"><div class="icon-art" role="img" aria-label="Job board clipboard illustration" style="background:linear-gradient(#7cc45a,#2c7a26)"></div>ACTIVE JOB BOARD</div>

<div class="orange-area" style="top:298px;height:219px"></div>
<div class="step" style="left:132px;width:172px"><div class="step-num">1</div><b>POST</b><span>A JOB</span></div>
<div class="step" style="left:324px;width:172px"><div class="step-num">2</div><b>GET</b><span>AS MANY<br>QUOTES AS YOU LIKE</span></div>
<div class="step" style="left:519px;width:170px"><div class="step-num">3</div><b>SELECT</b><span>ENERGY QUOTE<br>THAT SUITS</span></div>
<div class="step" style="left:708px;width:172px"><div class="step-num">4</div><b>APPROVE</b><span>PAYMENT</span></div>
<div class="step" style="left:901px;width:172px"><div class="step-num">5</div><b>RECEIVE</b><span>RATING</span></div>
<div class="step-glow" style="left:132px;width:172px"></div><div class="step-glow" style="left:324px;width:172px"></div><div class="step-glow" style="left:519px;width:170px"></div><div class="step-glow" style="left:708px;width:172px"></div><div class="step-glow" style="left:901px;width:172px"></div>
<div class="fade" style="top:517px;height:54px"></div>

<h2 class="head" style="left:148px;top:572px">Welcome To Our Site</h2>
<div class="copy" style="left:148px;top:624px;width:336px">
<p><strong>voltis australia</strong> is Australia's leading professional energy rating consultancy firm specializing in large scaled residential and commercial energy rating logistics.</p>
<p>We have professional and accredited energy raters in all States and Territories ready and waiting to provide quotes for and perform your energy rating jobs!</p>
<p>It's Free, Fast and Easy to use and you get the best price and turnaround time that suits you!!</p>
</div>
<div class="photo" role="img" aria-label="Photo of a smiling business team seated at a table" style="left:498px;top:625px;width:218px;height:145px"></div>
<div class="copy" style="left:148px;top:793px;width:570px">Register with us, upload your job and specifications, and sit back and watch as energy raters provide quotes for your work!</div>
<ul class="bullets">
<li>Get the best priced quotes for your energy ratings</li>
<li>Save time by listing a job to get many quotes</li>
<li>Monitor your jobs and quotes on your own job board</li>
<li>Be notified via email of all new quotes as they come in</li>
<li>Be able to specify your desired turnaround times</li>
<li>Accessible anytime and anywhere</li>
<li>Choose a deadline for energy raters to supply quotes</li>
<li>Have access to many qualified energy raters in your state all quoting for Work</li>
<li>Be able to track your jobs and pay online</li>
<li>Provide feedback on energy raters</li>
</ul>
<div class="copy" style="left:148px;top:1122px;width:570px">Its totally free to be registered with us and there is no obligations or hidden catches! So if you wish to utilise the amazing opportunity register now! This new website will be going live on the (insert date) so be ready to save some money!</div>

<div class="box" style="top:575px;height:223px">
<div class="box-head">Member Area</div>
<div class="field-label">Login id</div><div class="field"></div>
<div class="field-label" style="margin-top:10px">Password</div><div class="field" style="margin-top:8px"></div>
<div style="text-align:right;font-size:10px;margin:6px 28px 0 0">Forgot Pasword?</div>
<span class="btn-green" style="width:98px;height:28px;line-height:28px;margin:8px auto 0;font-size:12px">Sign in</span>
</div>
<div class="box" style="top:829px;height:315px">
<div class="box-head">Testimonials</div>
<div class="testi">
<p>Lorem Ipsum is simply dummy text of the printing and typesetting industry. Lorem Ipsum has been the industry's standard dummy text ever since the 1500s.</p>
<p><b>By: Liam Ford</b></p>
<p>When an unknown printer took a galley of type and scrambled it to make a type specimen book. It has survived not only five centuries.</p>
<p><b>By: Nora Pike</b></p>
</div>
</div>
<footer class="footer" style="top:1238px"><span>Home</span>|<span>How it works?</span>|<span>About Us</span>|<span>Testimonials</span>|<span>Contact Us</span></footer>

<!-- INNER PAGE -->
<div class="page-title" style="top:1320px">INNER PAGE</div>
<div class="green-bar" style="top:1406px"></div>
<div class="dark-band" style="top:1610px;height:192px"></div>
<div class="footer-side" style="top:2683px"></div>
<div class="frame" style="top:1427px;height:1297px"></div>
<div class="header-bg" style="top:1427px;height:178px"></div>
<nav class="nav" style="top:1427px"><span>HOME</span><span class="sep">|</span><span>HOW IT WORKS?</span><span class="sep">|</span><span>ABOUT US</span><span class="sep">|</span><span>TESTIMONIALS</span><span class="sep">|</span><span>CONTACT US</span></nav>
<div class="logo-box" style="top:1427px;height:176px"><div class="logo-dot"></div><div class="logo-name">voltis<br><span style="font-size:22px;letter-spacing:2px">australia</span></div></div>
<div class="user-links"><span>Client Name</span>|<span>Messages</span>|<span>Signout</span></div>

<div class="orange-area" style="top:1605px;height:197px"></div>
<div class="history">
<div class="portrait">Photograph</div>
<h3>Cleint History</h3>
<ul><li>Total Number of Projects:</li><li>Total Active Projects:</li><li>Feedback:</li><li>Responces:</li></ul>
</div>
<div class="fade" style="top:1802px;height:48px"></div>

<h2 class="head" style="left:148px;top:1860px">My Acount</h2>
<div class="edit-btn">Edit Profile</div>
<table class="account">
<tr><td class="label">Company Details:</td><td class="value">Joe Bloggs</td></tr>
<tr><td class="label">Contact Person:</td><td class="value"></td></tr>
<tr><td class="label">Email Address:</td><td class="value"></td></tr>
<tr><td class="label">Street Address:</td><td class="value">Level 1</td></tr>
<tr><td class="label"></td><td class="value">12 Harbour Lane</td></tr>
<tr><td class="label">Suburb:</td><td class="value">Elmwood</td></tr>
<tr><td class="label">State:</td><td class="value">VIC</td></tr>
<tr><td class="label">Postcode:</td><td class="value">3999</td></tr>
</table>

<div class="tab on" style="left:148px;width:219px">JOBS FOR QUOTING</div>
<div class="tab off" style="left:376px;width:218px">ACTIVE JOBS</div>
<div class="tab off" style="left:604px;width:218px">COMPLETED JOBS</div>
<div class="jobs-panel">
<h4>Currently Jobs for Quoting:</h4>
<table class="jobs">
<colgroup><col style="width:152px"><col style="width:105px"><col style="width:84px"><col style="width:97px"><col style="width:111px"><col style="width:96px"><col style="width:105px"><col style="width:69px"><col style="width:64px"></colgroup>
<thead><tr><th>JOB</th><th>QUOTE<br>NUMBER</th><th>PRICE</th><th>TOTAL<br>PRICE</th><th>TURNAROUND<br>TIME</th><th>REWORK<br>PRICE</th><th>ENERGY RATERS<br>ACCREDITATION</th><th>STATUS</th><th>EMAIL</th></tr></thead>
<tbody>
<tr><td></td><td>111111</td><td>$ 155.00</td><td>$ 180.65</td><td>1-5 days</td><td>$ 120.00</td><td>VIC</td><td><span class="mini">Accept</span></td><td><span class="mini" style="width:48px">Email</span></td></tr>
<tr><td></td><td>111156</td><td>$ 250.00</td><td>$ 265.00</td><td>5-10 days</td><td>$ 150.00</td><td>QLD</td><td><span class="mini">Accept</span></td><td><span class="mini" style="width:48px">Email</span></td></tr>
<tr><td></td><td>111186</td><td>$ 125.00</td><td>$ 129.65</td><td>2 weeks</td><td>$ 100.00</td><td>SA</td><td><span class="mini">Accept</span></td><td><span class="mini" style="width:48px">Email</span></td></tr>
<tr><td></td><td></td><td></td><td></td><td></td><td></td><td></td><td><span class="mini">Accept</span></td><td><span class="mini" style="width:48px">Email</span></td></tr>
<tr><td></td><td></td><td></td><td></td><td></td><td></td><td></td><td><span class="mini">Accept</span></td><td><span class="mini" style="width:48px">Email</span></td></tr>
<tr><td></td><td>111111</td><td>$ 155.00</td><td>$ 180.65</td><td>1-5 days</td><td>$ 120.00</td><td>VIC</td><td><span class="mini">Accept</span></td><td><span class="mini" style="width:48px">Email</span></td></tr>
<tr><td></td><td>111156</td><td>$ 250.00</td><td>$ 265.00</td><td>5-10 days</td><td>$ 150.00</td><td>QLD</td><td><span class="mini">Accept</span></td><td><span class="mini" style="width:48px">Email</span></td></tr>
<tr><td></td><td>111186</td><td>$ 125.00</td><td>$ 129.65</td><td>2 weeks</td><td>$ 100.00</td><td>SA</td><td><span class="mini">Accept</span></td><td><span class="mini" style="width:48px">Email</span></td></tr>
<tr><td></td><td>111313</td><td>$ 350.00</td><td>$ 354.65</td><td>Aluminium</td><td>Doors</td><td>Standard</td><td><span class="mini">Accept</span></td><td><span class="mini" style="width:48px">Email</span></td></tr>
</tbody>
</table>
</div>
<footer class="footer" style="top:2683px"><span>Home</span>|<span>How it works?</span>|<span>About Us</span>|<span>Testimonials</span>|<span>Contact Us</span></footer>

</body>
</html>
```